Trailbend Gear Depot

Design a new website design for www.trailbendgeardepot.com,

Target Market(s)

Men & Ladies

Industry/Entity Type

Side X side, ATV Offroad

Coding

Coded - Design and coding required

Number of Pages Required

1 page

```html
<!DOCTYPE html>
<html lang="en">
<head>
<meta charset="utf-8">
<title>Trailbend Gear Depot</title>
<link href="https://fonts.googleapis.com/css2?family=Poppins:wght@400;500;600;700;800&family=Roboto+Slab:wght@700;800&display=swap" rel="stylesheet">
<style>
:root{
  --ink:#111;
  --dark:#222;
  --panel:#333;
  --grey:#f2f2f2;
  --card:#ececec;
  --muted:#555;
  --white:#fff;
  --line:#d6d6d6;
}
*{box-sizing:border-box;margin:0;padding:0}
html,body{width:1200px;height:4494px;overflow:hidden}
body{font-family:'Poppins',sans-serif;color:var(--ink);background:var(--white);position:relative}
a{color:inherit;text-decoration:none}
.wrap{width:1050px;margin:0 auto;position:relative}

.topbar{height:61px;background:var(--dark);color:var(--white);font-size:16px;font-weight:500;display:flex;align-items:center;justify-content:center}

.header{height:105px;display:flex;align-items:center}
.header .wrap{display:flex;align-items:center}
.logo{font-weight:700;font-size:31px;line-height:1.12;color:#3a3a3a;width:240px;letter-spacing:.5px}
.search{margin-left:0;width:718px;height:57px;border:1px solid var(--line);border-radius:30px;display:flex;align-items:center;padding:0 20px;font-size:14px;color:#444;justify-content:space-between}
.icons{display:flex;gap:26px;margin-left:22px}

.nav{height:59px;background:var(--grey);display:flex;align-items:center;justify-content:center;gap:58px;font-size:19px;font-weight:500;color:#222}

.hero{height:649px;background:linear-gradient(100deg,#3c4031 0%,#5a5a46 40%,#4b4838 70%,#2d2f26 100%);position:relative}
.hero-text{position:absolute;left:75px;top:170px;color:var(--white)}
.hero h1{font-size:54px;font-weight:800;line-height:1.14}
.hero h2{font-size:35px;font-weight:700;line-height:1.26;margin-top:6px}
.btn-dark{display:inline-block;margin-top:26px;background:#111;color:var(--white);font-weight:600;font-size:20px;padding:12px 40px;border-radius:30px}
.dots{position:absolute;left:75px;top:584px;display:flex;gap:12px}
.dots i{width:8px;height:8px;border-radius:50%;background:var(--white);opacity:.7}
.dots i:first-child{opacity:1}

.section-title{font-size:38px;font-weight:500;text-align:center}
.arrow{position:absolute;top:50%;width:18px;height:30px}
.arrow.l{left:-33px}.arrow.r{right:-33px}

.categories{height:434px;padding-top:37px}
.cat-row{display:flex;gap:29px;margin-top:40px;position:relative}
.cat{width:241px;height:241px;background:var(--card);border-radius:6px;position:relative}
.cat .ph{position:absolute;left:20px;right:20px;top:20px;height:150px;border-radius:4px;background:radial-gradient(circle,#5c5650 0%,#cfcac2 55%,var(--card) 75%)}
.cat span{position:absolute;left:22px;bottom:16px;font-size:27px;font-weight:600}

.products{height:600px;padding-top:52px}
.products.alt{background:var(--grey)}
.prod-row{display:flex;gap:29px;margin-top:45px;position:relative}
.prod{width:241px;text-align:center}
.prod .ph{height:262px;background:var(--white);border-radius:8px;display:flex;align-items:center;justify-content:center}
.prod .ph i{display:block;width:170px;height:130px;border-radius:40px;background:radial-gradient(ellipse,#a8a196 0%,#d9d4cb 50%,var(--white) 75%)}
.products.pop .prod .ph{background:var(--grey)}
.prod .name{font-size:15px;color:var(--muted);line-height:1.55;margin-top:20px}
.prod .price{font-size:18px;font-weight:600;margin-top:14px}
.prod .seller{font-size:13px;color:#333;margin-top:4px}

.brands{height:433px;background:linear-gradient(120deg,#1b1b1b,#3a3a3a 50%,#1e1e1e);color:var(--white);padding-top:118px}
.brands .section-title{font-weight:600}
.brand-row{display:flex;justify-content:center;gap:35px;margin-top:40px}
.brand-btn{width:282px;height:103px;border:2px solid #bbb;display:flex;align-items:center;justify-content:center;font-family:'Roboto Slab',serif;font-weight:800;font-size:22px;letter-spacing:.5px}

.blog{height:649px;padding-top:46px}
.blog-row{display:flex;gap:31px;margin-top:42px}
.post{width:330px}
.post .ph{height:230px;background:linear-gradient(160deg,#8a7a5a,#3a3a33 60%,#6c6550)}
.post:nth-child(2) .ph{background:linear-gradient(160deg,#3d6a45,#4a4a48 55%,#8a8a86)}
.post:nth-child(3) .ph{background:linear-gradient(160deg,#5a7fa8,#444 55%,#2e2e2e)}
.post h3{font-size:24px;font-weight:600;line-height:1.3;margin-top:22px}
.post p{font-size:15px;color:#555;line-height:1.85;margin-top:10px}
.post .more{font-size:14px;font-weight:600;margin-top:14px;display:block}

.newsletter{height:268px;margin:0 auto;width:1050px;background:var(--panel);border-radius:6px;color:var(--white);text-align:center;padding-top:44px}
.newsletter h2{font-size:38px;font-weight:500}
.newsletter p{font-size:15px;margin-top:12px}
.form{display:flex;width:630px;margin:32px auto 0;height:54px}
.form .field{flex:1;background:var(--white);color:#444;font-size:14px;text-align:left;padding:17px 24px;border-radius:30px 0 0 30px}
.form .go{width:160px;background:#000;border-radius:0 30px 30px 0;font-weight:600;font-size:16px;display:flex;align-items:center;justify-content:center;gap:10px}

.footer{position:absolute;left:0;top:3936px;width:1200px;height:455px;background:var(--dark);color:var(--white)}
.cols{display:flex;padding-top:78px}
.col h4{font-size:23px;font-weight:600;margin-bottom:14px}
.col li{list-style:none;font-size:15px;line-height:38px}
.col.c1{width:267px}.col.c2{width:275px}.col.c3{width:282px}
.contact{font-size:15px;line-height:1.5}
.contact div{margin-bottom:20px}
.socials{display:flex;gap:18px}
.socials i{width:22px;height:22px;border-radius:4px;background:var(--white);display:block}

.bottom{position:absolute;left:0;top:4391px;width:1200px;height:103px;display:flex;align-items:center}
.bottom .wrap{display:flex;justify-content:space-between;align-items:center}
.copy{font-size:14px;color:#222}
.pay{display:flex;gap:9px}
.pay i{width:40px;height:24px;border-radius:4px;border:1px solid #ccc;background:#e7e7e7;display:block}
.pay i:nth-child(odd){background:#cfd6e4}
.mark{position:absolute;right:6px;top:57px;font-size:13px;color:#444}
</style>
</head>
<body>

<div class="topbar">Neque porro quisquam est, qui dolorem</div>

<header class="header">
  <div class="wrap">
    <div class="logo">TRAILBEND GEAR<br>DEPOT</div>
    <div class="search">Search
      <svg width="18" height="18" viewBox="0 0 20 20"><circle cx="8" cy="8" r="6" fill="none" stroke="#111" stroke-width="3"/><line x1="12.5" y1="12.5" x2="18" y2="18" stroke="#111" stroke-width="3"/></svg>
    </div>
    <div class="icons">
      <svg width="20" height="20" viewBox="0 0 20 20"><circle cx="10" cy="6" r="4.5" fill="#222"/><path d="M2 19c0-5 4-7 8-7s8 2 8 7z" fill="#222"/></svg>
      <svg width="22" height="20" viewBox="0 0 22 20"><path d="M1 7h20l-3 11H4z" fill="#222"/><path d="M6 7l5-6 5 6" fill="none" stroke="#222" stroke-width="2"/></svg>
    </div>
  </div>
</header>

<nav class="nav">
  <a>Audio</a><a>Ridgeline</a><a>Northstar</a><a>Hikari</a><a>Kazemoto</a><a>Heim Joints</a><a>Spacers</a>
</nav>

<section class="hero" role="img" aria-label="Off-road side by side vehicle parked on a forest trail among tall pine trees">
  <div class="hero-text">
    <h1>Welcome to<br>TRAILBEND GEAR DEPOT</h1>
    <h2>Ball Joints, Gears, Portals,<br>Music Roofs</h2>
    <a class="btn-dark">Shop Now</a>
  </div>
  <div class="dots"><i></i><i></i><i></i><i></i></div>
</section>

<section class="categories">
  <div class="wrap">
    <h2 class="section-title">Categories</h2>
    <div class="cat-row">
      <svg class="arrow l" viewBox="0 0 18 30"><path d="M14 4L4 15l10 11" fill="none" stroke="#222" stroke-width="2"/></svg>
      <div class="cat"><div class="ph" role="img" aria-label="Pair of audio speakers"></div><span>Audio</span></div>
      <div class="cat"><div class="ph" role="img" aria-label="Ball joints"></div><span>Ridgeline</span></div>
      <div class="cat"><div class="ph" role="img" aria-label="Pair of ball joints with boots"></div><span>Northstar</span></div>
      <div class="cat"><div class="ph" role="img" aria-label="Single ball joint"></div><span>Hikari</span></div>
      <svg class="arrow r" viewBox="0 0 18 30"><path d="M4 4l10 11L4 26" fill="none" stroke="#222" stroke-width="2"/></svg>
    </div>
  </div>
</section>

<section class="products alt">
  <div class="wrap">
    <h2 class="section-title">New Products</h2>
    <div class="prod-row">
      <svg class="arrow l" style="top:190px" viewBox="0 0 18 30"><path d="M14 4L4 15l10 11" fill="none" stroke="#222" stroke-width="2"/></svg>
      <div class="prod"><div class="ph" role="img" aria-label="Pair of heim joints"><i></i></div><p class="name">Pair Of 7/8" Bore X 7/8" Shank Heim Joints, 1.25" Od Tube Insert &amp; Jam Nut</p><p class="price">$89.99</p><p class="seller">Pivot Link Supply</p></div>
      <div class="prod"><div class="ph" role="img" aria-label="Set of heim joints in rows"><i></i></div><p class="name">Pair Of 7/8" Bore X 7/8" Shank Heim Joints, 1.25" Od Tube Insert &amp; Jam Nut</p><p class="price">$89.99</p><p class="seller">Pivot Link Supply</p></div>
      <div class="prod"><div class="ph" role="img" aria-label="Group of heim joints"><i></i></div><p class="name">Pair Of 7/8" Bore X 7/8" Shank Heim Joints, 1.25" Od Tube Insert &amp; Jam Nut</p><p class="price">$89.99</p><p class="seller">Pivot Link Supply</p></div>
      <div class="prod"><div class="ph" role="img" aria-label="Four heim joints"><i></i></div><p class="name">Pair Of 7/8" Bore X 7/8" Shank Heim Joints, 1.25" Od Tube Insert &amp; Jam Nut</p><p class="price">$89.99</p><p class="seller">Pivot Link Supply</p></div>
      <svg class="arrow r" style="top:190px" viewBox="0 0 18 30"><path d="M4 4l10 11L4 26" fill="none" stroke="#222" stroke-width="2"/></svg>
    </div>
  </div>
</section>

<section class="brands" role="img" aria-label="Dark close-up of off-road suspension shock absorber">
  <h2 class="section-title">Shop By Brands</h2>
  <div class="brand-row">
    <a class="brand-btn">TRAILBEND GEAR</a>
    <a class="brand-btn">DUST CREW</a>
    <a class="brand-btn">PIVOT LINK SUPPLY</a>
  </div>
</section>

<section class="products pop">
  <div class="wrap">
    <h2 class="section-title">Most Popular Products</h2>
    <div class="prod-row">
      <svg class="arrow l" style="top:190px" viewBox="0 0 18 30"><path d="M14 4L4 15l10 11" fill="none" stroke="#222" stroke-width="2"/></svg>
      <div class="prod"><div class="ph" role="img" aria-label="Aluminium spacers"><i></i></div><p class="name">Pair Of 7/8" Bore X 7/8" Shank Heim Joints, 1.25" Od Tube Insert &amp; Jam Nut</p><p class="price">$89.99</p><p class="seller">Pivot Link Supply</p></div>
      <div class="prod"><div class="ph" role="img" aria-label="Pair of bronze heim joints"><i></i></div><p class="name">Pair Of 7/8" Bore X 7/8" Shank Heim Joints, 1.25" Od Tube Insert &amp; Jam Nut</p><p class="price">$89.99</p><p class="seller">Pivot Link Supply</p></div>
      <div class="prod"><div class="ph" role="img" aria-label="Brass washers"><i></i></div><p class="name">Pair Of 7/8" Bore X 7/8" Shank Heim Joints, 1.25" Od Tube Insert &amp; Jam Nut</p><p class="price">$89.99</p><p class="seller">Pivot Link Supply</p></div>
      <div class="prod"><div class="ph" role="img" aria-label="Steel spacer rings"><i></i></div><p class="name">Pair Of 7/8" Bore X 7/8" Shank Heim Joints, 1.25" Od Tube Insert &amp; Jam Nut</p><p class="price">$89.99</p><p class="seller">Pivot Link Supply</p></div>
      <svg class="arrow r" style="top:190px" viewBox="0 0 18 30"><path d="M4 4l10 11L4 26" fill="none" stroke="#222" stroke-width="2"/></svg>
    </div>
  </div>
</section>

<section class="blog">
  <div class="wrap">
    <h2 class="section-title">Latest Blog Articles</h2>
    <div class="blog-row">
      <article class="post"><div class="ph" role="img" aria-label="Quad bike on desert sand dunes"></div><h3>Sed ut perspiciatis unde omnis iste natus.</h3><p>Neque porro quisquam est commodo enim ipsam voluptatem quia voluptas sit aspernatur aut odit aut fugita</p><a class="more">Read More &#8594;</a></article>
      <article class="post"><div class="ph" role="img" aria-label="Mechanic working on an ATV engine"></div><h3>Sed ut perspiciatis unde omnis iste natus.</h3><p>Neque porro quisquam est commodo enim ipsam voluptatem quia voluptas sit aspernatur aut odit aut fugita</p><a class="more">Read More &#8594;</a></article>
      <article class="post"><div class="ph" role="img" aria-label="Side by side vehicle in a rocky landscape"></div><h3>Sed ut perspiciatis unde omnis iste natus.</h3><p>Neque porro quisquam est commodo enim ipsam voluptatem quia voluptas sit aspernatur aut odit aut fugita</p><a class="more">Read More &#8594;</a></article>
    </div>
  </div>
</section>

<section class="newsletter">
  <h2>Newsletter Signup</h2>
  <p>Neque porro quisquam est commodo &nbsp;enim ipsam voluptatem quia voluptas sit aspernatur aut odit aut fugita</p>
  <div class="form"><div class="field">Enter Email Address</div><div class="go">Subscribe &#8594;</div></div>
</section>

<footer class="footer">
  <div class="wrap cols">
    <div class="col c1"><h4>Categories</h4><ul><li>Audio</li><li>Ridgeline</li><li>Northstar</li><li>Hikari</li><li>Kazemoto</li><li>Heim Joints</li><li>Spacers</li></ul></div>
    <div class="col c2"><h4>Brands</h4><ul><li>Pivot Link Supply</li><li>Dust Crew Offroad</li><li>Trailbend Gear Depot</li><li>View All</li></ul></div>
    <div class="col c3"><h4>Informations</h4><ul><li>Shipping &amp; Returns</li><li>Contact Us</li><li>Sitemap</li></ul></div>
    <div class="col"><h4>Contact Us</h4>
      <div class="contact"><div>1820 Ridge Rd Ste 4<br>Marlow, TX 75001</div><div>5550142278</div><div>info@trailbendgeardepot.com</div></div>
      <div class="socials"><i></i><i></i><i></i><i></i><i></i></div>
    </div>
  </div>
</footer>

<div class="bottom">
  <div class="wrap">
    <div class="copy">© Copyright 2024 Trailbend Gear Depot All Right Reserved</div>
    <div class="pay"><i></i><i></i><i></i><i></i><i></i><i></i><i></i><i></i><i></i><i></i><i></i></div>
  </div>
  <span class="mark">x10</span>
</div>

</body>
</html>
```